Stationery Design Project

I want to create a single page award for our top sales reps.

I want it to look like a diploma - but with a new school (modern) look and feel, not like a classic diploma.

Corlane is the top Home automation and Solar provider in North America, and our sales team of 2700 reps is amongst the best in the world. This award will recognize our sales reps for "Outstanding Achievment in Professional Sales"

Link to Website:
http://www.corlane-example.ca

The copy will be as follows:

Logo: corlane
This Award Certifies That:
"Lena Dubrow" has demonstrated "Outstanding Achievment in Professional Sales by closing:

"60 Funded Accounts"

Red Deer Alberta 2012

Sales Manager: Peter Halvik
_________________________

Sales Manger: Owen Tracey
_________________________

VP of Sales, Canada: Grant Ellisworth
__________________________

Industry/Entity Type

School

Requirements
Must have
• Corlane Logo

```html
<!DOCTYPE html>
<html lang="en">
<head>
<meta charset="utf-8">
<title>Corlane Sales Award</title>
<link href="https://fonts.googleapis.com/css2?family=Open+Sans:ital,wght@0,300;0,400;0,600;0,700;1,600&display=swap" rel="stylesheet">
<style>
  :root {
    --paper: #ffffff;
    --orange: #f7931e;
    --ink: #2b2b2b;
    --muted: #9a9a9a;
    --light: #c4c4c4;
  }
  * { margin: 0; padding: 0; box-sizing: border-box; }
  html, body { width: 1200px; height: 842px; overflow: hidden; background: var(--paper); }
  body { font-family: "Open Sans", Arial, sans-serif; color: var(--ink); }

  .award { position: relative; width: 1200px; height: 842px; background: var(--paper); }

  .side-band { position: absolute; left: 0; top: 0; width: 44px; height: 842px; background: var(--orange); }

  .company-name { position: absolute; left: 70px; top: 30px; font-size: 20px; font-weight: 400; color: var(--ink); letter-spacing: 1px; line-height: 1; }
  .top-rule { position: absolute; left: 220px; right: 0; top: 40px; height: 16px; background: var(--orange); }

  .title { position: absolute; left: 200px; top: 150px; font-size: 96px; font-weight: 300; color: var(--light); letter-spacing: 2px; line-height: 1; }

  .eyebrow { position: absolute; left: 204px; font-size: 15px; font-weight: 600; text-transform: uppercase; letter-spacing: 2px; color: var(--muted); }
  .eyebrow--certifies { top: 312px; }
  .eyebrow--demonstrated { top: 428px; }

  .recipient { position: absolute; left: 200px; top: 330px; font-size: 66px; font-weight: 400; color: var(--ink); line-height: 1.2; }

  .achievement { position: absolute; left: 204px; top: 462px; font-size: 24px; font-weight: 600; font-style: italic; color: var(--ink); }

  .result { position: absolute; left: 204px; top: 520px; color: var(--orange); font-weight: 700; text-transform: uppercase; display: flex; align-items: baseline; gap: 12px; }
  .result__count { font-size: 60px; line-height: 1; }
  .result__label { font-size: 30px; letter-spacing: 1px; }

  .signatures { position: absolute; left: 204px; top: 670px; list-style: none; }
  .signature { font-size: 15px; color: var(--muted); margin-bottom: 20px; display: flex; align-items: flex-end; gap: 12px; }
  .signature__line { display: inline-block; width: 260px; border-bottom: 1px solid var(--light); height: 16px; }

  .issued { position: absolute; right: 60px; top: 772px; font-size: 14px; color: var(--muted); }
</style>
</head>
<body>
  <main class="award">
    <div class="side-band"></div>
    <div class="company-name">Corlane</div>
    <div class="top-rule"></div>

    <h1 class="title">AWARD</h1>

    <p class="eyebrow eyebrow--certifies">This Award Certifies That</p>
    <p class="recipient">Lena Dubrow</p>
    <p class="eyebrow eyebrow--demonstrated">Has Demonstrated</p>
    <p class="achievement">"Outstanding Achievement in Professional Sales by closing:</p>
    <p class="result"><span class="result__count">60</span><span class="result__label">Funded Accounts</span></p>

    <ul class="signatures">
      <li class="signature">Sales Manager: Peter Halvik <span class="signature__line"></span></li>
      <li class="signature">Sales Manager: Owen Tracey <span class="signature__line"></span></li>
      <li class="signature">VP of Sales, Canada: Grant Ellisworth <span class="signature__line"></span></li>
    </ul>

    <p class="issued">Red Deer, Alberta 2012</p>
  </main>
</body>
</html>
```